Hi,
We are an accounting firm looking to upgrade the following:
Logo, letterhead, withcomp slips and maybe our business cards. I have attached our original letterhead (sample A) and a letterhead (SAmple B) which we like the design and layout, however I want to stick with the colours of our orginal letterhead (Sample A) but improve and modernise the look with other letter head (Sample B) I have attached both. On the footer of Sample A, we would like to remove the names of the directors but leave EST. 1985 we also want to add the QRT logo ABN and TAX AGENT logo as stated in Sample B , we would like to do a layout for the header similar to SAmple B however maybe a bit more structured.

```html
<!DOCTYPE html>
<html lang="en">
<head>
<meta charset="utf-8">
<title>Brentholm Accountants Letterhead</title>
<link rel="stylesheet" href="https://fonts.googleapis.com/css2?family=Montserrat:wght@500;600;700&display=swap">
<style>
  :root {
    --navy: #1b3a57;
    --brand: #173e73;
    --bright-blue: #2a7fc6;
    --text: #1f2a3a;
    --icon: #1d4380;
    --rule: #cfd3d8;
    --paper: #fdfdfd;
    --edge: #d4d4d4;
    --badge-blue: #0f56a0;
    --badge-yellow: #f8d20c;
    --badge-orange: #f0913a;
    --badge-green: #c8e03a;
  }
  * { margin: 0; padding: 0; box-sizing: border-box; }
  html, body { width: 849px; height: 1200px; overflow: hidden; background: #ffffff; }
  .letterhead {
    position: relative;
    width: 849px;
    height: 1200px;
    background: var(--paper);
    border: 1px solid var(--edge);
    font-family: "Montserrat", sans-serif;
    color: var(--text);
    overflow: hidden;
  }
  .brand {
    position: absolute;
    left: 46px;
    top: 34px;
    display: flex;
    align-items: center;
    gap: 12px;
    color: var(--brand);
    font-weight: 700;
  }
  .brand-mark { width: 16px; height: 16px; background: var(--brand); }
  .brand-name { line-height: 1; }
  .brand-name .primary { display: block; font-size: 46px; letter-spacing: -1px; }
  .brand-name .secondary { display: block; font-size: 26px; margin-top: 6px; }
  .contact {
    position: absolute;
    right: 34px;
    top: 55px;
    text-align: right;
    font-size: 13.4px;
    font-weight: 500;
    line-height: 19.5px;
    white-space: nowrap;
  }
  .contact-line { display: flex; justify-content: flex-end; align-items: center; gap: 12px; }
  .contact-item { display: inline-flex; align-items: center; gap: 5px; }
  .contact-item svg { fill: var(--icon); }
  .header-rule {
    position: absolute;
    left: 35px;
    right: 34px;
    top: 123px;
    height: 1px;
    background: var(--rule);
  }
  .accreditations {
    position: absolute;
    top: 1094px;
    left: 608px;
    display: flex;
    align-items: center;
    gap: 10px;
  }
  .footer-band { position: absolute; left: 0; top: 1143px; }
  .established {
    position: absolute;
    left: 57px;
    top: 1151px;
    color: #ffffff;
    font-size: 14px;
    font-weight: 600;
    letter-spacing: 0.5px;
  }
</style>
</head>
<body>
<main class="letterhead">
  <header>
    <div class="brand">
      <span class="brand-mark"></span>
      <div class="brand-name">
        <span class="primary">Brentholm</span>
        <span class="secondary">Accountants</span>
      </div>
    </div>

    <address class="contact" style="font-style:normal">
      <div class="contact-line">
        <span class="contact-item">
          <svg width="10" height="11" viewBox="0 0 24 24"><path d="M6.6 10.8c1.4 2.8 3.8 5.1 6.6 6.6l2.2-2.2c.3-.3.7-.4 1-.2 1.1.4 2.3.6 3.6.6.6 0 1 .4 1 1V20c0 .6-.4 1-1 1C10.6 21 3 13.4 3 4c0-.6.4-1 1-1h3.5c.6 0 1 .4 1 1 0 1.3.2 2.5.6 3.6.1.3 0 .7-.2 1z"/></svg>
          +61 3 9000 1234
        </span>
        <span class="contact-item">
          <svg width="13" height="12" viewBox="0 0 26 24"><path d="M7 1h12v6h5v16H2V7h5zm2 2v4h8V3zM4 9v12h18V9zm3 3h2v7H7zm4 0h2v7h-2zm4 0h2v7h-2zm4 0h1v7h-1z"/></svg>
          +61 3 9000 5678
        </span>
      </div>
      <div class="contact-line">
        <span class="contact-item">
          <svg width="11" height="8" viewBox="0 0 22 16"><path d="M0 0h22v16H0zm2 2v1l9 6 9-6V2zm0 3.4V14h18V5.4l-9 6z"/></svg>
          info@brentholm.com.au
        </span>
        <span class="contact-item">
          <svg width="10" height="10" viewBox="0 0 24 24"><path d="M12 1a11 11 0 1 0 0 22 11 11 0 0 0 0-22zm-1 2.1V7H7.6c.8-2.1 2-3.6 3.4-3.9zm2 0c1.4.3 2.6 1.8 3.4 3.9H13zM5.4 7H3.9A9 9 0 0 1 8 3.6 12 12 0 0 0 5.4 7zm13.2 0A12 12 0 0 0 16 3.6 9 9 0 0 1 20.1 7zM3.2 9h2c-.1 1-.2 2-.2 3h-2c0-1 .1-2 .2-3zm4 0H11v3H7c0-1 .1-2 .2-3zM13 9h3.8c.1 1 .2 2 .2 3h-4zm5.8 0h2a9 9 0 0 1 .2 3h-2c0-1-.1-2-.2-3zM3 14h2c0 1 .1 2 .3 3h-1.4A9 9 0 0 1 3 14zm4 0h4v3H7.3C7.1 16 7 15 7 14zm6 0h4c0 1-.1 2-.3 3H13zm6 0h2a9 9 0 0 1-.9 3h-1.4c.2-1 .3-2 .3-3zM4.9 19h1.5A12 12 0 0 0 8 20.4 9 9 0 0 1 4.9 19zm3.4 0H11v1.9C9.9 20.6 9 20 8.3 19zm4.7 0h2.7c-.7 1-1.6 1.6-2.7 1.9zm4.6 0h1.5a9 9 0 0 1-3.1 1.4c.6-.4 1.1-.9 1.6-1.4z"/></svg>
          www.brentholmaccountants.com.au
        </span>
      </div>
      <div class="contact-line">
        <span class="contact-item">
          <svg width="10" height="13" viewBox="0 0 20 26"><path d="M10 0a9 9 0 0 0-9 9c0 6.8 9 17 9 17s9-10.2 9-17a9 9 0 0 0-9-9zm0 2.2A6.8 6.8 0 0 1 16.8 9c0 4.2-4.6 10.6-6.8 13.4C7.8 19.6 3.2 13.2 3.2 9A6.8 6.8 0 0 1 10 2.2zM10 5.5a3.5 3.5 0 1 0 0 7 3.5 3.5 0 0 0 0-7z"/></svg>
          Brentholm Pty Ltd, ABN 12 345 678 901 210 Elmore Street Ashvale Vic. 3199
        </span>
      </div>
    </address>

    <div class="header-rule"></div>
  </header>

  <section class="accreditations">
    <svg width="88" height="38" viewBox="0 0 88 38" role="img" aria-label="Professional body membership badge">
      <rect x="0" y="0" width="55" height="38" fill="var(--badge-blue)"/>
      <rect x="55" y="0" width="33" height="38" fill="var(--badge-yellow)"/>
    </svg>
    <svg width="66" height="39" viewBox="0 0 66 39" role="img" aria-label="Business register listing badge">
      <rect x="0" y="0" width="66" height="39" rx="3" fill="var(--badge-orange)"/>
    </svg>
    <svg width="46" height="46" viewBox="0 0 46 46" role="img" aria-label="Registered tax agent badge">
      <circle cx="23" cy="23" r="21.5" fill="#ffffff" stroke="#555" stroke-width="1"/>
      <circle cx="23" cy="23" r="12" fill="var(--badge-green)"/>
    </svg>
  </section>

  <footer>
    <svg class="footer-band" width="849" height="34" viewBox="0 0 849 34">
      <polygon points="0,0 552,0 518,34 0,34" fill="var(--navy)"/>
      <polygon points="568,0 568,34 535,34" fill="var(--navy)"/>
      <rect x="568" y="0" width="281" height="34" fill="var(--bright-blue)"/>
    </svg>
    <p class="established">EST. 1985</p>
  </footer>
</main>
</body>
</html>
```